Velmora Interiors Stationary Set

Velmora Interiors is a bespoke interior design firm set to provide services to VIP clients with elegance and minimalism is the main theme for our stationary set. We require a full stationary set covering A4 letterhead, A4 & A3 envelopes, business cards, USB's, CDs, email signature and any other item the designer sees fit. logo is already designed and finalized, and we require the designer to use it as is without modifying the logo.

Address to be used on letterhead / business cards ...etc shall be as follows:

Phone : +971 2 518 3074
P.O. Box : 609318
Address: Block C&D, Bldg. 27, Court 14, Abu Dhabi, United Arab Emirates
Website: www.velmorainteriors-example.com

Target Market(s)

VIP Clients

Industry/Entity Type

Interior Design

Other font styles liked:
• something to be unique

Colors

Designer to choose colors to be used in the design.

Requirements
Must have
• Elegant, minimalistic
Nice to have
• Simple yet elegant design having a sharp yet clean cut format
Should not have
• No additional colours, just colours that are used in the logo (silver, black or gold)

```html
<!DOCTYPE html>
<html lang="en">
<head>
<meta charset="utf-8">
<title>Velmora Interiors Stationery Set</title>
<link rel="stylesheet" href="https://fonts.googleapis.com/css2?family=Cormorant+Garamond:wght@500&family=Inter:wght@400;500&display=swap">
<style>
  :root {
    --backdrop: #8b8b8a;
    --charcoal: #575755;
    --charcoal-edge: #4d4d4b;
    --paper: #fbfbfa;
    --gold: #b9a56c;
    --gold-deep: #8c7f59;
    --gold-liner: #a89a72;
    --ink: #3a3a3a;
  }
  html, body { margin: 0; padding: 0; overflow: hidden; }
  body { width: 1200px; height: 1048px; background: var(--backdrop); }
  .canvas { position: relative; width: 1200px; height: 1048px; background: var(--backdrop); overflow: hidden; }
  .item { position: absolute; box-sizing: border-box; }
  .sheet { background: var(--paper); }
  .board { background: var(--charcoal); }

  .wordmark {
    position: absolute;
    font-family: "Cormorant Garamond", Georgia, serif;
    font-weight: 500;
    color: var(--gold);
    line-height: 1;
    white-space: nowrap;
    letter-spacing: 0.04em;
  }
  .wordmark .name { display: block; font-size: 1em; }
  .wordmark .sub { display: block; font-size: 0.42em; letter-spacing: 0.32em; margin-top: 3px; padding-left: 1.4em; }

  .small-print {
    font-family: "Inter", Arial, sans-serif;
    font-weight: 400;
    font-size: 4px;
    line-height: 1.5;
    white-space: nowrap;
  }

  /* letterhead */
  .letterhead { left: 122px; top: 77px; width: 293px; height: 413px; }
  .letterhead .wordmark { left: 22px; top: 26px; font-size: 15px; }
  .letterhead-footer { position: absolute; left: 20px; bottom: 13px; padding-left: 6px; border-left: 1.5px solid var(--gold); color: var(--ink); }

  /* envelopes */
  .envelope-open { left: 459px; top: 132px; width: 307px; height: 210px; }
  .envelope-front { left: 802px; top: 132px; width: 306px; height: 154px; }
  .envelope-front .wordmark { left: 36px; top: 99px; font-size: 12px; }
  .envelope-back { left: 802px; top: 330px; width: 308px; height: 155px; }
  .envelope-back .return-address { position: absolute; left: 0; right: 0; top: 26px; text-align: center; color: var(--gold); }
  svg { display: block; }

  /* business cards */
  .card { top: 415px; width: 118px; height: 76px; }
  .card-front { left: 460px; }
  .card-front .wordmark { left: 36px; top: 26px; font-size: 13px; }
  .card-back { left: 598px; }
  .card-details { position: absolute; left: 0; right: 0; top: 20px; text-align: center; color: var(--gold); }
  .card-details .person { font-size: 4.6px; font-weight: 500; letter-spacing: 0.04em; }
  .card-details .gap { height: 5px; }

  /* closed folder */
  .folder-cover { left: 98px; top: 534px; width: 319px; height: 426px; box-shadow: 0 1px 2px rgba(0,0,0,0.15); }
  .folder-cover .wordmark { left: 202px; top: 46px; font-size: 17px; }

  /* open folder */
  .folder-open { left: 464px; top: 529px; width: 640px; height: 428px; }
  .folder-panel { position: absolute; top: 0; width: 320px; height: 428px; background: var(--charcoal); }
  .folder-panel.left { left: 0; }
  .folder-panel.right { left: 320px; border-left: 1px solid var(--charcoal-edge); }
  .folder-insert { position: absolute; left: 340px; top: 9px; width: 292px; height: 300px; background: var(--paper); }
  .folder-insert .wordmark { left: 24px; top: 22px; font-size: 15px; }
  .folder-pockets { position: absolute; left: 0; top: 0; }
  .folder-open .pocket-mark { left: 542px; top: 370px; font-size: 15px; }
</style>
</head>
<body>
<main class="canvas">

  <section class="item sheet letterhead" aria-label="Letterhead">
    <div class="wordmark"><span class="name">Velmora</span><span class="sub">INTERIORS</span></div>
    <div class="letterhead-footer small-print">
      Block C&amp;D, Bldg. 27, Court 14, Abu Dhabi, United Arab Emirates<br>
      P.O. Box: 609318 · Tel: +971 2 518 3074 · www.velmorainteriors-example.com
    </div>
  </section>

  <section class="item envelope-open" aria-label="Open envelope with gold liner">
    <svg width="307" height="210" viewBox="0 0 307 210">
      <rect x="0" y="0" width="307" height="42" fill="var(--gold-liner)"/>
      <rect x="0" y="0" width="307" height="6" fill="var(--gold-deep)"/>
      <polygon points="0,42 307,42 307,210 0,210" fill="var(--charcoal)"/>
      <polygon points="18,42 289,42 276,66 31,66" fill="#cbbf98"/>
      <polygon points="0,42 31,66 276,66 307,42 307,210 0,210" fill="var(--charcoal)"/>
    </svg>
  </section>

  <section class="item board envelope-front" aria-label="Envelope front">
    <div class="wordmark"><span class="name">Velmora</span><span class="sub">INTERIORS</span></div>
  </section>

  <section class="item envelope-back" aria-label="Envelope back">
    <svg width="308" height="155" viewBox="0 0 308 155">
      <rect x="0" y="0" width="308" height="155" fill="var(--charcoal)"/>
      <polygon points="0,0 308,0 296,52 168,62 140,62 12,52" fill="#5c5c5a"/>
      <polyline points="0,0 12,52 140,62 168,62 296,52 308,0" fill="none" stroke="var(--charcoal-edge)" stroke-width="1"/>
    </svg>
    <div class="return-address small-print">
      Block C&amp;D, Bldg. 27, Court 14, Abu Dhabi, United Arab Emirates<br>
      P.O. Box: 609318 · www.velmorainteriors-example.com
    </div>
  </section>

  <section class="item board card card-front" aria-label="Business card front">
    <div class="wordmark"><span class="name">Velmora</span><span class="sub">INTERIORS</span></div>
  </section>

  <section class="item board card card-back" aria-label="Business card back">
    <div class="card-details small-print">
      <div class="person">NADIA FARROW</div>
      <div>Design Director</div>
      <div class="gap"></div>
      <div>T: +971 2 518 3074</div>
      <div>www.velmorainteriors-example.com</div>
      <div class="gap"></div>
      <div>Block C&amp;D, Bldg. 27, Court 14</div>
      <div>Abu Dhabi, United Arab Emirates</div>
    </div>
  </section>

  <section class="item board folder-cover" aria-label="Presentation folder cover">
    <div class="wordmark"><span class="name">Velmora</span><span class="sub">INTERIORS</span></div>
  </section>

  <section class="item folder-open" aria-label="Open presentation folder">
    <div class="folder-panel left"></div>
    <div class="folder-panel right"></div>
    <div class="folder-insert">
      <div class="wordmark"><span class="name">Velmora</span><span class="sub">INTERIORS</span></div>
    </div>
    <svg class="folder-pockets" width="640" height="428" viewBox="0 0 640 428">
      <path d="M0,296 L12,290 L300,290 Q306,290 308,296 L312,428 L0,428 Z" fill="#5a5a58" stroke="var(--charcoal-edge)" stroke-width="1"/>
      <path d="M328,428 L332,296 Q334,290 340,290 L628,290 L640,296 L640,428 Z" fill="#5a5a58" stroke="var(--charcoal-edge)" stroke-width="1"/>
      <line x1="320" y1="0" x2="320" y2="428" stroke="var(--charcoal-edge)" stroke-width="1"/>
    </svg>
    <div class="wordmark pocket-mark"><span class="name">Velmora</span><span class="sub">INTERIORS</span></div>
  </section>

</main>
</body>
</html>
```